Website Design for a Chemical Sales Company

We are working with a Chemical Sales Company in California. They sell various chemicals throughout the US.
Types of products they sell: https://www.harborveilguard.example/us/products/all
https://www.vexalink.example/products/kuvo/kuvochill-glycol-thermal-fluids/kuvochill-propylene-glycol-thermal-fluids
Some sites to use for inspiration:
https://www.vexalink.example
https://www.kuvo.example/en-us
Thank you for taking the time to consider designing a website for us. We are web developers based in Stockton, CA, USA. Most of our projects go through the same process. Understanding this process may help you win a project with us. We custom-code all of our websites in-house. We don’t have any requirements as to what tools you use for your design, but we ask that you follow these guidelines.
IMAGES:
If you use any images or icons in the design, we ask that you have a link to the asset so we can purchase the image/icon. Most of the designs we submit do not have the customer’s images on them unless they have some great images. Be creative; show us the feeling you are trying to portray with your image choices. Use any royalty-free site you choose. We subscribe to Pellum and mainly use their images, but we can purchase images outside of Pellum. PLEASE NOTE: we will not submit designs to clients with watermarks on the images.
FONTS:
We ask that you identify the fonts you’re using in the design. This can be done in a message if you want. We typically use Zarvik Fonts and Pellum Fonts.
CONTENT:
We're always open to different content and ideas. We often submit designs with stock images so the client can see our vision. We typically take pictures after the website launch to use their images with our vision. Lorem Ipsum is fine for paragraphs, but we ask that you make the Headers with correct English. We want to be able to show the vision and identify the sections of the website.
INSPIRATION:
We typically add a couple of links in the brief of websites we like to help you get started in your design.
REVISIONS:
We do not often ask for revisions of the designs unless we see something in the design that may not appeal to the client. If there are slight changes that we want to make, we do that in the development process.
FEEDBACK:
We rarely give feedback on designs during the design process. We are working on many website projects and do not have the time to provide feedback. We usually respond if your request is well thought out and asks specific questions, but a note asking “feedback, please” usually goes unanswered.

```html
<!DOCTYPE html>
<html lang="en">
<head>
<meta charset="utf-8">
<title>Ionvale Supply</title>
<link href="https://fonts.googleapis.com/css2?family=Montserrat:wght@400;500;600;700;800&family=Lato:wght@300;400&display=swap" rel="stylesheet">
<style>
:root{
  --blue:#0d8fd9;
  --blue-dark:#0a78c0;
  --ink:#111;
  --grey:#555;
  --line:#cfcfcf;
  --white:#fff;
  --black:#000;
}
*{box-sizing:border-box;margin:0;padding:0}
html,body{width:1200px;height:3236px;overflow:hidden;background:var(--white)}
body{position:relative;font-family:"Montserrat",sans-serif;color:var(--ink)}
.abs{position:absolute}
a{color:inherit;text-decoration:none}

/* header */
.site-header{left:0;top:0;width:1200px;height:107px}
.brand{display:flex;align-items:center;gap:8px;font-family:"Montserrat",sans-serif;font-weight:500;font-size:20px;color:var(--blue);white-space:nowrap}
.brand-dot{width:14px;height:14px;border-radius:50%;background:var(--blue)}
.site-header .brand{left:98px;top:40px}
.nav a{font-family:"Lato",sans-serif;font-size:17px;color:#222;top:39px}
.search{left:622px;top:30px;width:292px;height:41px;border:2px solid var(--blue-dark);border-radius:21px;font-family:"Lato",sans-serif;font-size:17px;color:#333;padding:8px 0 0 12px}
.search svg{position:absolute;right:14px;top:11px}
.call{left:938px;top:39px;font-family:"Lato",sans-serif;font-size:17px;color:#222}

/* hero */
.hero{left:0;top:107px;width:1200px;height:564px;background:linear-gradient(90deg,#eef2f7 0%,#e6edf4 38%,#cfdbe8 60%,#b9cbdd 100%)}
.hero-photo{left:540px;top:107px;width:660px;height:564px;background:radial-gradient(ellipse at 55% 45%,#e3e8ee 0%,#c8d3df 50%,#a9bcd0 100%)}
.hero-kicker{left:104px;top:240px;font-size:35px;font-weight:500}
.hero-title{left:103px;top:292px;font-size:49px;font-weight:700;color:var(--blue);letter-spacing:.5px}
.hero-text{left:104px;top:362px;width:420px;font-size:16px;line-height:26px;color:#222}
.btn{display:flex;align-items:center;justify-content:center;background:var(--blue);color:var(--white);border-radius:40px;font-weight:600}
.hero-btn{left:105px;top:456px;width:159px;height:51px;font-size:17px}
.feature{width:223px;height:233px;top:513px;background:var(--white);border-radius:12px;box-shadow:0 4px 14px rgba(0,0,0,.12);padding:16px 14px 16px 25px}
.feature-icon{width:55px;height:55px;border-radius:50%;background:var(--blue);display:flex;align-items:center;justify-content:center}
.feature h3{font-size:19px;font-weight:500;line-height:26px;margin-top:18px}
.feature p{font-size:10px;line-height:15px;color:#555;margin-top:12px;padding-right:8px}

/* section headings */
.section-title{display:flex;align-items:center;gap:18px;font-size:38px;font-weight:700}
.section-title::after{content:"";width:42px;height:3px;background:var(--blue-dark)}

/* products */
.product{width:242px;height:288px;border:2px solid var(--line);background:var(--white)}
.product-img{position:absolute;left:80px;top:14px;width:80px;height:130px;border-radius:8px}
.product h4{position:absolute;left:18px;top:178px;font-size:12.5px;font-weight:600;text-transform:uppercase;white-space:nowrap}
.product p{position:absolute;left:18px;top:208px;width:210px;font-size:13px;line-height:20px;color:#555;font-weight:500}
.product .btn{position:absolute;left:20px;top:268px;width:130px;height:38px;font-size:13px}
.view-all{left:456px;top:1663px;width:287px;height:64px;font-size:18px}

/* account band */
.account{left:0;top:1830px;width:1200px;height:503px;background:linear-gradient(90deg,#1b8ed6 0%,#2c93d6 40%,#5aa9df 70%,#7fbde6 100%)}
.account-photo{left:560px;top:1830px;width:640px;height:503px;background:radial-gradient(ellipse at 50% 60%,rgba(210,232,248,.7) 0%,rgba(120,180,225,.4) 45%,rgba(40,140,210,0) 80%)}
.account-kicker{left:100px;top:1892px;display:flex;align-items:center;gap:12px;font-size:22px;font-weight:500;color:var(--white)}
.account-kicker::after{content:"";width:54px;height:2px;background:var(--white)}
.account-title{left:99px;top:1938px;font-size:40px;font-weight:700;line-height:50px;color:var(--white)}
.account-text{left:100px;top:2062px;width:420px;font-size:15.5px;line-height:26px;font-weight:500;color:var(--white)}
.read-more{left:99px;top:2199px;width:183px;height:57px;background:var(--black);font-size:21px;font-weight:500}

/* partners */
.partner{top:2507px;width:238px;height:208px;background:var(--white);border-radius:10px;box-shadow:0 3px 12px rgba(0,0,0,.1);display:flex;align-items:center;justify-content:center}
.partner-mark{width:110px;height:110px;border-radius:50%;background:linear-gradient(135deg,#2b4a6b,#4a9ad8)}
.partner-mark.square{border-radius:14px;background:#d7e6f3}
.partner-mark.small{width:90px;height:90px;background:#cfe9f7}

/* footer */
.site-footer{left:0;top:2836px;width:1200px;height:400px;background:var(--black)}
.footer-brand{left:95px;top:2984px;font-size:28px;font-weight:500;color:var(--white);display:flex;align-items:center;gap:12px;white-space:nowrap}
.footer-brand .brand-dot{width:20px;height:20px;background:var(--white)}
.footer-col{color:var(--white)}
.footer-col h5{font-size:19px;font-weight:700;letter-spacing:.3px}
.footer-col ul{list-style:none;margin-top:26px}
.footer-col li{font-size:15px;font-weight:500;line-height:29px;display:flex;align-items:center;gap:14px}
.footer-col li::before{content:"›";color:var(--blue);font-size:16px}
.contact li::before{content:none}
.contact li{align-items:flex-start;gap:20px;line-height:22px;margin-bottom:16px}
.contact svg{flex:none;margin-top:4px}
.footer-rule{left:98px;top:3143px;width:1004px;height:1px;background:#888}
.copyright{left:0;top:3167px;width:1200px;text-align:center;font-size:15px;font-weight:500;color:var(--white)}
</style>
</head>
<body>

<header class="abs site-header">
  <a class="abs brand" href="#"><span>IONVALE SUPPLY</span><span class="brand-dot"></span></a>
  <nav class="nav">
    <a class="abs" style="left:325px" href="#">Products</a>
    <a class="abs" style="left:434px" href="#">Learn</a>
    <a class="abs" style="left:520px" href="#">Company</a>
  </nav>
  <div class="abs search">Search
    <svg width="16" height="16" viewBox="0 0 16 16"><circle cx="6.5" cy="6.5" r="5" fill="none" stroke="#111" stroke-width="2.2"/><path d="M10 10l4.5 4.5" stroke="#111" stroke-width="2.4" stroke-linecap="round"/></svg>
  </div>
  <div class="abs call">Call : +1 555-014-2200</div>
</header>

<section>
  <div class="abs hero"></div>
  <div class="abs hero-photo" role="img" aria-label="Scientist in lab coat and safety goggles holding two flasks of blue and green liquid"></div>
  <div class="abs hero-kicker">WELCOME TO</div>
  <h1 class="abs hero-title">IONVALE SUPPLY</h1>
  <p class="abs hero-text">Lorem ipsum dolor sit amet, consectetur adipiscing elit, sed do eiusmod tempor incididunt ut labore et dolore magna aliqua.</p>
  <a class="abs btn hero-btn" href="#">Get Started</a>

  <div class="abs feature" style="left:630px">
    <div class="feature-icon"><svg width="30" height="30" viewBox="0 0 30 30" fill="none" stroke="#fff" stroke-width="1.6" stroke-linejoin="round"><path d="M3 13l6-6 5 3 4-3 9 7-4 4"/><path d="M9 16l4 4 3-2 3 3 4-4"/><path d="M3 13l4 4"/></svg></div>
    <h3>Become a<br>Producer Partner</h3>
    <p>Lorem ipsum dolor sit amet, consectetur adipiscing elit, sed do eiusmod tempor incididunt ut labore et dolore magna aliqua.</p>
  </div>
  <div class="abs feature" style="left:877px">
    <div class="feature-icon"><svg width="30" height="30" viewBox="0 0 30 30" fill="none" stroke="#fff" stroke-width="1.6" stroke-linejoin="round"><path d="M10 6l5-3 5 3v6l-5 3-5-3z"/><path d="M4 14v8l7 5M26 14v8l-7 5"/></svg></div>
    <h3>Find the Right<br>Product</h3>
    <p>Lorem ipsum dolor sit amet, consectetur adipiscing elit, sed do eiusmod tempor incididunt ut labore et dolore magna aliqua.</p>
  </div>
</section>

<section>
  <h2 class="abs section-title" style="left:101px;top:832px">All Products</h2>

  <div class="abs product" style="left:99px;top:917px"><div class="product-img" role="img" aria-label="Black magnetic filter unit with valves" style="background:linear-gradient(#555,#222)"></div><h4>Clearflow Vortex</h4><p>Filter for powerful magnetic filtration of system debris</p><a class="btn" href="#">View Products</a></div>
  <div class="abs product" style="left:352px;top:917px"><div class="product-img" role="img" aria-label="Red power flushing machine" style="background:linear-gradient(#f05a3a,#c92a14)"></div><h4>PurgeJet C90</h4><p>Effective, easy cleaning for dirty heating systems</p><a class="btn" href="#">View Products</a></div>
  <div class="abs product" style="left:605px;top:917px"><div class="product-img" role="img" aria-label="Blue carry case test kit" style="left:55px;width:130px;top:30px;height:100px;background:linear-gradient(#2f6fd0,#1a4aa0)"></div><h4>PurgeJet Test Kit</h4><p>For identifying problem areas on old hydronic heating</p><a class="btn" href="#">View Products</a></div>
  <div class="abs product" style="left:857px;top:917px"><div class="product-img" role="img" aria-label="White container of solar thermal fluid" style="background:linear-gradient(#f4f6f8,#d9dde2)"></div><h4>S100 Solar Thermal Fluid</h4><p>Ready-to-use heat transfer fluid for solar thermal systems</p><a class="btn" href="#">View Products</a></div>

  <div class="abs product" style="left:99px;top:1284px"><div class="product-img" role="img" aria-label="Two white containers of solar cleaner" style="left:50px;width:140px;background:linear-gradient(#f2f4f6,#d5dae0)"></div><h4>S200 Solar Cleaner</h4><p>Ready-to-use cleaner for solar thermal systems</p><a class="btn" href="#">View Products</a></div>
  <div class="abs product" style="left:352px;top:1284px"><div class="product-img" role="img" aria-label="Teal labelled container of system cleaner" style="background:linear-gradient(#7fe0e0,#3cc2c8)"></div><h4>Harborveil H400 Cleaner</h4><p>For older closed loop hydronic heating systems</p><a class="btn" href="#">View Products</a></div>
  <div class="abs product" style="left:605px;top:1284px"><div class="product-img" role="img" aria-label="Yellow labelled container of inhibitor" style="background:linear-gradient(#f7e24a,#e5c21a)"></div><h4>H100 Inhibitor</h4><p>For protecting closed loop hydronic heating systems</p><a class="btn" href="#">View Products</a></div>
  <div class="abs product" style="left:857px;top:1284px"><div class="product-img" role="img" aria-label="Yellow aerosol canister with red dosing nozzle" style="left:100px;width:40px;background:linear-gradient(#e8342a,#f5d51e)"></div><h4>H100 Inhibitor Quick-Dose</h4><p>Quickly dose systems for protection of closed loop</p><a class="btn" href="#">View Products</a></div>

  <a class="abs btn view-all" href="#">View All&nbsp; Products</a>
</section>

<section>
  <div class="abs account"></div>
  <div class="abs account-photo" role="img" aria-label="Glass laboratory flasks with clear liquid on a blue background"></div>
  <div class="abs account-kicker">My Ionvale Supply</div>
  <h2 class="abs account-title">Online access to<br>your account</h2>
  <p class="abs account-text">Lorem ipsum dolor sit amet, consectetur adipiscing elit, sed do eiusmod tempor incididunt ut labore et dolore magna aliqua. empor incididunt ut labore etempor incididunt ut labore et</p>
  <a class="abs btn read-more" href="#">Read More</a>
</section>

<section>
  <h2 class="abs section-title" style="left:101px;top:2410px">Our Partner</h2>
  <div class="abs partner" style="left:100px"><div class="partner-mark square" style="width:120px;height:70px"></div></div>
  <div class="abs partner" style="left:354px"><div class="partner-mark"></div></div>
  <div class="abs partner" style="left:608px"><div class="partner-mark small"></div></div>
  <div class="abs partner" style="left:862px"><div class="partner-mark square small"></div></div>
</section>

<footer>
  <div class="abs site-footer"></div>
  <div class="abs footer-brand"><span>IONVALE SUPPLY</span><span class="brand-dot"></span></div>

  <div class="abs footer-col" style="left:455px;top:2922px">
    <h5>QUICK LINK</h5>
    <ul><li>Products</li><li>Learn</li><li>Company</li></ul>
  </div>
  <div class="abs footer-col" style="left:616px;top:2922px">
    <h5>HELP LINKS</h5>
    <ul><li>Terms &amp; Conditions</li><li>Privacy Policy</li><li>About Us</li><li>Support</li></ul>
  </div>
  <div class="abs footer-col contact" style="left:837px;top:2922px;width:270px">
    <h5>CONTACT US</h5>
    <ul style="margin-top:24px">
      <li><svg width="14" height="16" viewBox="0 0 14 16"><path d="M7 1a5 5 0 0 0-5 5c0 4 5 9 5 9s5-5 5-9a5 5 0 0 0-5-5z" fill="#0d8fd9"/><circle cx="7" cy="6" r="2" fill="#000"/></svg><span>Lorem ipsum dolor sit amet, consectetur adipiscing</span></li>
      <li><svg width="14" height="14" viewBox="0 0 14 14"><path d="M3 1l2.5 3-1.5 1.5a8 8 0 0 0 4.5 4.5L10 8.5l3 2.5-1.5 2A10 10 0 0 1 1 2.5z" fill="#0d8fd9"/></svg><span>+1 555-014-2200</span></li>
      <li><svg width="15" height="12" viewBox="0 0 15 12"><rect x="1" y="1" width="13" height="10" fill="none" stroke="#0d8fd9" stroke-width="1.4"/><path d="M1 1l6.5 5.5L14 1" fill="none" stroke="#0d8fd9" stroke-width="1.4"/></svg><span>info@ionvale.example</span></li>
    </ul>
  </div>

  <div class="abs footer-rule"></div>
  <div class="abs copyright">© copyrights 2023&nbsp; Ionvale Supply |&nbsp; All Rights Reserved</div>
</footer>

</body>
</html>
```